Organic Infographic – "The 4 Dimensions of Transformation"

Overview:
We are a coaching/education brand (Brightmoor Institute) and need a redesigned infographic illustrating our 4-area transformation model. Our current version (attached) uses a rigid, hard-edged triangle/pyramid layout — we want a completely new visual approach that feels organic, soft, and alive, since the topic is human personal development, not a technical process.

Content structure (please keep the wording, redesign the visual form):

4 areas: "Embodiment – The Foundation" and "Focus & Intuition Redefined – The Lens" sit on the same base level. "Heart Centered Living – The Bridge" sits one level above, connecting/enabling the other two. "Becoming Unlimited – The Peak" sits at the top, made possible by Heart Centered Living.
The 4 areas influence and inspire one another — this mutual connection must be visually recognizable (e.g. through overlapping zones, blended color transitions, connecting flowing lines, or similar). Areas may stay visually distinct; the connection between them is what must be shown.
Hierarchy should be expressed mainly through position/arrangement (ascending flow), not through size differences — all 4 areas should carry similar visual weight, since each is equally essential.
A supporting element: "The Brightmoor Methodology" with 3 phases (Phase 1: Awareness & Insight, Phase 2: Integration & Practice, Phase 3: Expansion & Sustainable Growth), each with a short description (text provided below).

Style direction:
Organic, soft, flowing shapes — no sharp angles or rigid geometric triangles. Attached are 3 moodboard references showing the direction we like: overlapping/blended circular shapes, flowing ribbon-style connections, and organic swirl divisions. Please don't copy any of them directly — combine this organic/overlapping visual language with our specific asymmetric hierarchy (2 areas base level + 1 bridge + 1 peak), which none of the references show exactly. This creative translation is the core task.

Icons: Please design one new, unified icon per area (4 total) plus 3 simple icons for the methodology phases — consistent style across all 7, your creative interpretation is welcome.

Typography: Headlines in Arsenal, body text in DM Sans.

Colors: Base palette — Embodiment D09176, Focus & Intuition Redefined B6623E, Heart Centered Living D9866B, Becoming Unlimited 6F7A70, dark text 23211A, light accent EACEC1. Slight adjustments are welcome if they improve visual distinction between areas.

Technical requirements (important):

Final files as vector format (SVG, AI, or EPS), with separated, editable, non-flattened/non-merged layers and paths.
Shapes should consist of simple, closed outline paths — no fine textures, no complex multi-stop gradients, no photorealistic rendering — since the artwork will later be manually redrawn as a whiteboard-animation video.
Primary format: 16:9 landscape. A secondary vertical/mobile version (3 outer areas stacked below the top area) is welcome but optional.

Usage rights: Full commercial usage across website, video, and social media required.

Attachments to include: current draft PDF (for text content and logo reference only — not for layout), our logo file, and the 3 moodboard reference images.

Budget: $100–150 — please let us know if this realistically allows for more designer participation, or advise on adjusting scope/budget

Methodology phase texts (for the 3 supporting icons):

Phase 1: Awareness & Insight
Cultivating self-reflection, identifying patterns, and gaining clarity on personal drivers through introspective practices and data-informed assessment.

Phase 2: Integration & Practice
Applying tools and frameworks, developing new habits, and aligning actions with core values through consistent application and feedback loops.

Phase 3: Expansion & Sustainable Growth
Achieving long-term transformation, exceeding limitations, and fostering resilience through continuous evolution and a purpose-driven approach.

```html
<!DOCTYPE html>
<html lang="en">
<head>
<meta charset="utf-8">
<title>The 4 Dimensions of Transformation – Brightmoor Institute</title>
<link href="https://fonts.googleapis.com/css2?family=Arsenal:ital,wght@0,400;0,700;1,400&family=DM+Sans:wght@400;600&display=swap" rel="stylesheet">
<style>
  :root {
    --embodiment: #D09176;
    --focus: #B6623E;
    --heart: #D9866B;
    --unlimited: #6F7A70;
    --unlimited-accent: #C67A5E;
    --text-dark: #23211A;
    --accent-light: #EACEC1;
    --band: #CF9176;
    --title-top: #B6623E;
    --title-bottom: #D08266;
    --logo-grey: #8E968F;
    --white: #FFFFFF;
    --bg: #FBFAF9;
  }
  * { margin: 0; padding: 0; box-sizing: border-box; }
  html, body { width: 1200px; height: 675px; overflow: hidden; background: var(--bg); }
  .canvas { position: relative; width: 1200px; height: 675px; overflow: hidden; background: var(--bg); font-family: "DM Sans", sans-serif; color: var(--text-dark); }

  .main-title { position: absolute; left: 70px; top: 38px; font-family: "Arsenal", sans-serif; font-weight: 700; line-height: 0.86; }
  .main-title .line-top { display: block; font-size: 60px; color: var(--title-top); letter-spacing: 0.3px; }
  .main-title .line-bottom { display: block; font-size: 62px; color: var(--title-bottom); margin-left: 9px; letter-spacing: 0.3px; }
  .main-title .connector { position: absolute; left: 205px; top: 36px; font-style: italic; font-weight: 400; font-size: 34px; line-height: 1; color: var(--unlimited); }

  .method-band { position: absolute; left: 609px; top: 0; width: 591px; height: 122px; background: var(--band); border-bottom-left-radius: 62px; }
  .method-title { position: absolute; left: 650px; top: 40px; font-family: "Arsenal", sans-serif; font-weight: 700; font-size: 40px; line-height: 1; color: var(--white); white-space: nowrap; }
  .method-title .accent { color: var(--unlimited); }

  .dimensions { position: absolute; left: 0; top: 0; }

  .dim-label { position: absolute; color: var(--white); }
  .dim-label .name { font-family: "Arsenal", sans-serif; font-weight: 700; font-size: 17px; line-height: 15px; display: block; }
  .dim-label .role { font-family: "DM Sans", sans-serif; font-weight: 400; font-size: 12px; line-height: 13px; display: block; margin-top: 3px; }
  .label-unlimited { left: 252px; top: 240px; }
  .label-heart { left: 260px; top: 368px; width: 140px; text-align: center; }
  .label-embodiment { left: 158px; top: 488px; }
  .label-focus { left: 392px; top: 488px; width: 110px; text-align: right; }

  .phase { position: absolute; left: 650px; width: 540px; height: 120px; }
  .phase-1 { top: 172px; }
  .phase-2 { top: 309px; }
  .phase-3 { top: 437px; }
  .phase-icon { position: absolute; left: 0; top: 0; }
  .phase-pill { position: absolute; left: 107px; top: 0; width: 93px; height: 25px; background: var(--unlimited); border-radius: 13px 13px 13px 0; color: var(--white); font-family: "Arsenal", sans-serif; font-weight: 700; font-size: 15px; line-height: 25px; text-align: center; }
  .phase-rule { position: absolute; left: 95px; top: 31px; height: 1px; background: var(--focus); }
  .phase-1 .phase-rule { width: 180px; }
  .phase-2 .phase-rule { width: 198px; }
  .phase-3 .phase-rule { width: 287px; }
  .phase-title { position: absolute; left: 109px; top: 35px; font-family: "Arsenal", sans-serif; font-weight: 700; font-size: 20.5px; color: var(--focus); white-space: nowrap; }
  .phase-text { position: absolute; left: 107px; top: 63px; width: 405px; font-size: 10.2px; line-height: 12.6px; font-weight: 600; color: var(--text-dark); }

  .brand { position: absolute; left: 663px; top: 569px; display: flex; align-items: center; }
  .brand-dot { width: 56px; height: 56px; border-radius: 50%; background: var(--embodiment); margin-right: 10px; }
  .brand-name { font-family: "Arsenal", sans-serif; font-weight: 400; font-size: 29px; color: var(--logo-grey); white-space: nowrap; }
</style>
</head>
<body>
<div class="canvas">

  <h1 class="main-title">
    <span class="line-top">The 4 Dimensions</span>
    <span class="line-bottom">Transformation</span>
    <span class="connector">of</span>
  </h1>

  <div class="method-band"></div>
  <h2 class="method-title">The Brightmoor <span class="accent">Methodology</span></h2>

  <svg class="dimensions" width="1200" height="675" viewBox="0 0 1200 675">
    <defs>
      <clipPath id="clip-embodiment"><circle cx="232" cy="530" r="100"/></clipPath>
      <clipPath id="clip-focus"><circle cx="428" cy="530" r="100"/></clipPath>
      <clipPath id="clip-heart"><circle cx="330" cy="400" r="100"/></clipPath>
      <clipPath id="clip-unlimited"><circle cx="330" cy="262" r="100"/></clipPath>
    </defs>

    <g class="dim-embodiment">
      <circle cx="232" cy="530" r="100" fill="var(--unlimited)"/>
      <g clip-path="url(#clip-embodiment)">
        <circle cx="116" cy="654" r="122" fill="#BF8068"/>
        <circle cx="120" cy="650" r="120" fill="var(--embodiment)"/>
      </g>
      <circle cx="232" cy="530" r="101.5" fill="none" stroke="var(--white)" stroke-width="4"/>
    </g>

    <g class="dim-focus">
      <circle cx="428" cy="530" r="100" fill="var(--unlimited)"/>
      <g clip-path="url(#clip-focus)">
        <circle cx="544" cy="654" r="122" fill="#A65535"/>
        <circle cx="540" cy="650" r="120" fill="var(--focus)"/>
      </g>
      <circle cx="428" cy="530" r="101.5" fill="none" stroke="var(--white)" stroke-width="4"/>
    </g>

    <g class="dim-heart">
      <circle cx="330" cy="400" r="100" fill="var(--unlimited)"/>
      <g clip-path="url(#clip-heart)">
        <circle cx="330" cy="536" r="112" fill="#C97A60"/>
        <circle cx="330" cy="540" r="110" fill="var(--heart)"/>
      </g>
      <circle cx="330" cy="400" r="101.5" fill="none" stroke="var(--white)" stroke-width="4"/>
    </g>

    <g class="dim-unlimited">
      <circle cx="330" cy="262" r="100" fill="var(--unlimited)"/>
      <g clip-path="url(#clip-unlimited)">
        <circle cx="454" cy="176" r="127" fill="#B56E54"/>
        <circle cx="450" cy="180" r="125" fill="var(--unlimited-accent)"/>
      </g>
      <circle cx="330" cy="262" r="101.5" fill="none" stroke="var(--white)" stroke-width="4"/>
    </g>

    <g class="dim-icons" fill="none" stroke="var(--white)" stroke-width="1.6">
      <g role="img" aria-label="Becoming Unlimited icon: radiant spiral sun">
        <circle cx="395" cy="225" r="26"/>
        <circle cx="395" cy="225" r="19" fill="var(--white)" fill-opacity="0.18" stroke="none"/>
      </g>
      <g role="img" aria-label="Heart Centered Living icon: figure with glowing heart">
        <circle cx="330" cy="464" r="26"/>
        <circle cx="330" cy="464" r="19" fill="var(--white)" fill-opacity="0.18" stroke="none"/>
      </g>
      <g role="img" aria-label="Embodiment icon: strong flexing figure">
        <circle cx="190" cy="590" r="26"/>
        <circle cx="190" cy="590" r="19" fill="var(--white)" fill-opacity="0.18" stroke="none"/>
      </g>
      <g role="img" aria-label="Focus and Intuition icon: radiant eye">
        <circle cx="470" cy="590" r="26"/>
        <circle cx="470" cy="590" r="19" fill="var(--white)" fill-opacity="0.18" stroke="none"/>
      </g>
    </g>
  </svg>

  <div class="dim-label label-unlimited"><span class="name">Becoming<br>Unlimited</span><span class="role">The Peak</span></div>
  <div class="dim-label label-heart"><span class="name">Heart Centered<br>Living</span><span class="role">The Bridge</span></div>
  <div class="dim-label label-embodiment"><span class="name">Embodiment</span><span class="role">The Foundation</span></div>
  <div class="dim-label label-focus"><span class="name">Focus &amp;<br>Intuition</span><span class="role">The Lens</span></div>

  <div class="phase phase-1">
    <svg class="phase-icon" width="100" height="96" viewBox="0 0 100 96">
      <path d="M1 45 A48 48 0 0 0 96 52" fill="none" stroke="var(--focus)" stroke-width="1"/>
      <circle cx="49" cy="41" r="38" fill="var(--heart)"/>
      <g role="img" aria-label="Phase 1 icon: figure with a light bulb idea">
        <circle cx="49" cy="41" r="23" fill="none" stroke="var(--white)" stroke-width="1.3"/>
      </g>
    </svg>
    <div class="phase-pill">Phase 1</div>
    <div class="phase-rule"></div>
    <div class="phase-title">Awareness &amp; Insight</div>
    <p class="phase-text">Cultivating self-reflection, identifying patterns and gaining clarity on personal drivers through introspective practices and data-informed assessment.</p>
  </div>

  <div class="phase phase-2">
    <svg class="phase-icon" width="100" height="96" viewBox="0 0 100 96">
      <path d="M1 45 A48 48 0 0 0 96 52" fill="none" stroke="var(--focus)" stroke-width="1"/>
      <circle cx="49" cy="41" r="38" fill="var(--heart)"/>
      <g role="img" aria-label="Phase 2 icon: head profile with turning gears">
        <circle cx="49" cy="41" r="23" fill="none" stroke="var(--white)" stroke-width="1.3"/>
      </g>
    </svg>
    <div class="phase-pill">Phase 2</div>
    <div class="phase-rule"></div>
    <div class="phase-title">Integration &amp; Practice</div>
    <p class="phase-text">Applying tools and frameworks, developing new habits and aligning actions with core values through consistent application and feedback loops.</p>
  </div>

  <div class="phase phase-3">
    <svg class="phase-icon" width="100" height="96" viewBox="0 0 100 96">
      <path d="M1 45 A48 48 0 0 0 96 52" fill="none" stroke="var(--focus)" stroke-width="1"/>
      <circle cx="49" cy="41" r="38" fill="var(--heart)"/>
      <g role="img" aria-label="Phase 3 icon: target with outward arrows">
        <circle cx="49" cy="41" r="23" fill="none" stroke="var(--white)" stroke-width="1.3"/>
      </g>
    </svg>
    <div class="phase-pill">Phase 3</div>
    <div class="phase-rule"></div>
    <div class="phase-title">Expansion &amp; Sustainable Growth</div>
    <p class="phase-text">Achieving long-term transformation, exceeding limitations, and fostering resilience through continuous evolution and a purpose-driven approach.</p>
  </div>

  <div class="brand">
    <span class="brand-dot"></span>
    <span class="brand-name">Brightmoor Institute</span>
  </div>

</div>
</body>
</html>
```